I need someone to help me finish my logo for Tavrin Honey and create a honey label template I can use and amend for each harvest.
I created some basic labels last year but I want the quality to be better as my partner made the logo in Word. I also want a label with more detail so I can sell the honey to local shops e.g. include nutritionals, ingredients, address. Visit tavrinhoney on instagram to see more and examples of last years label in situ.

```html
<!DOCTYPE html>
<html lang="en">
<head>
<meta charset="UTF-8">
<title>Tavrin Honey – Pure Raw Honey Label</title>
<link href="https://fonts.googleapis.com/css2?family=Open+Sans:wght@400;600;700&display=swap" rel="stylesheet">
<style>
  :root {
    --ink: #000000;
    --paper: #ffffff;
    --illustration-tone: #e4e4e4;
    --pattern-tone: #d6d6d6;
  }
  * { margin: 0; padding: 0; box-sizing: border-box; }
  html, body { width: 1200px; height: 1200px; overflow: hidden; background: var(--paper); }
  body { font-family: "Open Sans", Arial, sans-serif; color: var(--ink); }
  .label { position: relative; width: 1200px; height: 1200px; background: var(--paper); }

  .frame { position: absolute; inset: 0; }

  .bee-illustration {
    position: absolute; left: 89px; top: 117px; width: 566px; height: 461px;
    background: radial-gradient(ellipse at 45% 45%, var(--illustration-tone), var(--paper) 72%);
  }
  .honeycomb-pattern {
    position: absolute; left: 655px; top: 0; width: 545px; height: 500px;
    background: linear-gradient(200deg, var(--pattern-tone), var(--paper) 78%);
  }

  .brand-name {
    position: absolute; left: 548px; top: 400px;
    font-size: 139px; font-weight: 400; line-height: 1; letter-spacing: 1px;
  }
  .product-type {
    position: absolute; left: 554px; top: 555px;
    font-size: 62px; font-weight: 400; line-height: 1;
  }
  .description {
    position: absolute; left: 81px; top: 655px; width: 1054px;
    font-size: 18px; line-height: 33px; text-transform: uppercase;
    text-align: justify; text-align-last: justify; letter-spacing: 0.2px;
  }

  .rule { position: absolute; left: 81px; width: 1037px; height: 5px; background: var(--ink); }
  .rule-top { top: 784px; }
  .rule-bottom { top: 1012px; }

  .section-tag {
    position: absolute; background: var(--ink); color: var(--paper);
    font-size: 31px; line-height: 40px; height: 40px; padding: 0 8px; letter-spacing: 0.5px;
  }
  .tag-ingredients { left: 82px; top: 816px; }
  .tag-nutritional { left: 464px; top: 816px; }
  .tag-contact { left: 82px; top: 1059px; padding: 0 12px; }

  .column-divider { position: absolute; left: 394px; top: 817px; width: 3px; height: 170px; background: var(--ink); }

  .ingredient-list { position: absolute; left: 88px; top: 876px; list-style: none; }
  .ingredient-list li { font-size: 30px; line-height: 33.5px; }
  .ingredient-list li::before { content: "-"; display: inline-block; width: 38px; }

  .nutrition-table { position: absolute; left: 463px; top: 874px; width: 637px; height: 113px; }
  .nutrition-table .edge { position: absolute; top: 0; width: 1.5px; height: 113px; background: var(--ink); }
  .nutrition-table .cell-head {
    position: absolute; font-size: 17px; font-weight: 700; line-height: 1; text-align: center;
  }
  .nutrition-table .head-line { position: absolute; height: 1.5px; background: var(--ink); }
  .nutrition-table .cell-body { position: absolute; font-size: 15.5px; line-height: 26px; }

  .contact-list { position: absolute; top: 1058px; left: 350px; width: 770px; display: flex; justify-content: space-between; list-style: none; }
  .contact-list li { font-size: 30px; line-height: 40px; }
  .contact-list li::before { content: "- "; }
</style>
</head>
<body>
<main class="label">
  <div class="honeycomb-pattern" role="img" aria-label="Geometric honeycomb cube pattern in black line work"></div>
  <div class="bee-illustration" role="img" aria-label="Geometric low-poly line illustration of a honey bee in flight"></div>

  <svg class="frame" width="1200" height="1200" viewBox="0 0 1200 1200" aria-hidden="true">
    <polyline points="698,47 46,47 46,1154 1154,1154 1154,487" fill="none" stroke="#000" stroke-width="3"/>
  </svg>

  <h1 class="brand-name">TAVRIN</h1>
  <p class="product-type">PURE RAW HONEY</p>

  <p class="description">Lorem ipsum dolor sit amet, consectetuer adipiscing elit, sed diam nonummy nibh euismod tincidunt ut laoreet dolore magna aliquam erat volutpat. Ut wisi enim ad minim veniam, quis nostrud exerci tation ullamcorper suscipit lobortis nisl ut aliquip ex ea commodo consequat.</p>

  <div class="rule rule-top"></div>

  <h2 class="section-tag tag-ingredients">INGREDIENTS</h2>
  <ul class="ingredient-list">
    <li>Lorem ipsum</li>
    <li>Lorem ipsum</li>
    <li>Lorem ipsum</li>
  </ul>

  <div class="column-divider"></div>

  <h2 class="section-tag tag-nutritional">NUTRITIONAL</h2>
  <div class="nutrition-table">
    <span class="edge" style="left:0"></span>
    <span class="edge" style="left:176px"></span>
    <span class="edge" style="left:635px"></span>
    <span class="head-line" style="left:192px; top:0; width:429px"></span>
    <span class="cell-head" style="left:12px; top:10px; width:146px">LOREM IPSUM</span>
    <span class="head-line" style="left:12px; top:35px; width:148px"></span>
    <span class="cell-head" style="left:192px; top:10px; width:429px">LOREM IPSUM</span>
    <span class="head-line" style="left:192px; top:35px; width:429px"></span>
    <div class="cell-body" style="left:17px; top:52px">Lorem ipsum<br>Lorem ipsum</div>
    <div class="cell-body" style="left:192px; top:52px; width:429px; text-align:center">Lorem ipsum<br>Lorem ipsum</div>
  </div>

  <div class="rule rule-bottom"></div>

  <h2 class="section-tag tag-contact">CONTACT</h2>
  <ul class="contact-list">
    <li>Lorem ipsum</li>
    <li>Lorem ipsum</li>
    <li>Lorem ipsum</li>
  </ul>
</main>
</body>
</html>
```